Canadian Christian Church needs design for new sermon series

A graphic design for our series and an invitation card to invite people to the series. Check design brief for more detailed information. Target audience: young families and young adults. Looking for a creative design that will get people's attention and create interest. See design brief for copy of design purchased for previous series.
entered Apr 4 incorrectly. Need a week to receive and review designs, and today is Apr 2/19. Thanks!
young families and young adults

```html
<!DOCTYPE html>
<html lang="en">
<head>
<meta charset="utf-8">
<title>Messy – Sermon Series Invitation</title>
<link rel="stylesheet" href="https://fonts.googleapis.com/css2?family=Montserrat:wght@500;600;700&family=Libre+Baskerville:wght@400;700&family=Lato:wght@400&family=Yanone+Kaffeesatz:wght@400&display=swap">
<style>
  :root {
    --page-bg: #e1e1e1;
    --front-bg: #d9d3c7;
    --back-bg: #c2b8a2;
    --ink: #3a302c;
    --ink-soft: #4a3f39;
    --white: #ffffff;
    --photo-light: #c9c1b3;
    --photo-dark: #6f655b;
  }
  * { box-sizing: border-box; margin: 0; padding: 0; }
  html, body { width: 1200px; height: 1200px; overflow: hidden; background: var(--page-bg); }
  .canvas { position: relative; width: 1200px; height: 1200px; }

  .card { position: absolute; left: 296px; width: 609px; height: 480px; overflow: hidden; }
  .card--front { top: 120px; background: linear-gradient(180deg, #cfc8bb 0%, var(--front-bg) 45%, #ddd7cc 100%); }
  .card--back { top: 662px; background: linear-gradient(160deg, #ccc3ae 0%, var(--back-bg) 50%, #bdb29b 100%); }
  .card__curves { position: absolute; inset: 0; }

  .hero-photo {
    position: absolute; right: 0; top: 0; width: 330px; height: 480px;
    background: linear-gradient(90deg, rgba(201,193,179,0) 0%, var(--photo-light) 25%, #9e9487 60%, var(--photo-dark) 100%);
  }
  .front__frame { position: absolute; left: 9px; top: 13px; width: 592px; height: 456px; border: 1.5px solid var(--ink); }

  .church-mark { position: absolute; left: 32px; top: 62px; display: flex; flex-direction: column; align-items: center; gap: 6px; }
  .church-mark__dot { width: 62px; height: 62px; border-radius: 50%; background: var(--ink-soft); opacity: .85; }
  .church-mark__name { font-family: "Yanone Kaffeesatz", sans-serif; font-size: 18px; color: var(--ink); letter-spacing: .3px; }

  .series-title { position: absolute; left: 30px; top: 196px; font-family: "Montserrat", sans-serif; font-weight: 700; font-size: 100px; line-height: 1; color: var(--ink); letter-spacing: 1px; }
  .series-tagline {
    position: absolute; left: 33px; top: 288px; width: 443px; height: 45px; background: var(--ink);
    font-family: "Libre Baskerville", serif; font-weight: 700; font-size: 27px; color: var(--white);
    display: flex; align-items: center; padding-left: 16px; letter-spacing: -.3px;
  }
  .series-url { position: absolute; left: 32px; top: 418px; font-family: "Libre Baskerville", serif; font-size: 16px; color: var(--ink); letter-spacing: 2px; }

  .invite { position: absolute; left: 0; width: 100%; text-align: center; font-family: "Montserrat", sans-serif; font-weight: 700; color: var(--white); }
  .invite__title { top: 26px; font-size: 40px; line-height: 1; }
  .invite__time { top: 70px; font-size: 35px; line-height: 1; font-weight: 600; }

  .topics { position: absolute; left: 24px; top: 145px; width: 364px; font-family: "Montserrat", sans-serif; }
  .topics__label { display: inline-block; background: var(--ink); color: var(--white); font-weight: 600; font-size: 15px; letter-spacing: .5px; padding: 0 7px; height: 28px; line-height: 30px; }
  .topics__table { width: 364px; border-collapse: collapse; }
  .topics__table td { border: 1.5px solid var(--ink); height: 26px; color: var(--white); font-weight: 600; font-size: 16px; padding: 0 10px; line-height: 1; letter-spacing: .3px; }
  .topics__table td.topics__date { width: 122px; }

  .info { position: absolute; left: 415px; font-family: "Montserrat", sans-serif; color: var(--ink); }
  .info__heading { font-weight: 600; font-size: 16px; line-height: 1.25; letter-spacing: .3px; padding-bottom: 6px; border-bottom: 1px solid #f1ece2; width: 143px; }
  .info--features { top: 142px; }
  .info--about { top: 271px; }
  .info__list { list-style: none; margin-top: 12px; font-family: "Lato", sans-serif; font-size: 9px; line-height: 1.25; color: var(--ink-soft); }
  .info__list li { position: relative; padding-left: 8px; margin-bottom: 5px; width: 175px; }
  .info__list li::before { content: ""; position: absolute; left: 0; top: 4px; width: 3px; height: 3px; border-radius: 50%; background: var(--ink); }
  .info__text { margin-top: 10px; width: 170px; font-family: "Lato", sans-serif; font-size: 7px; line-height: 1.35; color: var(--ink-soft); }

  .contact-bar {
    position: absolute; left: 0; bottom: 0; width: 100%; height: 60px; background: var(--ink);
    color: var(--white); font-family: "Montserrat", sans-serif; font-weight: 500; font-size: 12.5px; text-align: center;
    display: flex; flex-direction: column; justify-content: center; gap: 4px;
  }
</style>
</head>
<body>
<div class="canvas">

  <section class="card card--front">
    <svg class="card__curves" width="609" height="480" viewBox="0 0 609 480" aria-hidden="true">
      <path d="M60 0 C 220 120, 380 200, 609 150" fill="none" stroke="#efeae1" stroke-width="1.2" opacity=".6"/>
      <path d="M0 210 C 80 120, 200 80, 380 70" fill="none" stroke="#efeae1" stroke-width="1" opacity=".5"/>
      <path d="M0 360 C 60 420, 120 460, 160 480" fill="none" stroke="#efeae1" stroke-width="1" opacity=".5"/>
    </svg>
    <div class="hero-photo" role="img" aria-label="Sepia photograph of a woman in a wheelchair stopped at the foot of outdoor steps under a cloudy sky"></div>
    <div class="front__frame"></div>
    <div class="church-mark">
      <span class="church-mark__dot"></span>
      <span class="church-mark__name">Maple Grove Family Church</span>
    </div>
    <h1 class="series-title">MESSY</h1>
    <p class="series-tagline">JOINING GOD IN THE MESS</p>
    <p class="series-url">www.mgfamilychurch.ca</p>
  </section>

  <section class="card card--back">
    <svg class="card__curves" width="609" height="480" viewBox="0 0 609 480" aria-hidden="true">
      <path d="M10 0 C 90 120, 250 180, 609 170" fill="none" stroke="#ddd5c4" stroke-width="1.2" opacity=".6"/>
      <path d="M300 0 C 420 60, 520 70, 609 40" fill="none" stroke="#ddd5c4" stroke-width="1" opacity=".5"/>
    </svg>
    <p class="invite invite__title">JOIN US</p>
    <p class="invite invite__time">Sundays @ 10:30</p>

    <div class="topics">
      <span class="topics__label">MESSAGE TOPICS</span>
      <table class="topics__table">
        <tr><td class="topics__date">April 28th</td><td>We Made This Mess</td></tr>
        <tr><td class="topics__date">May 5th</td><td>Bless in the Mess</td></tr>
        <tr><td class="topics__date">May 12th</td><td>Born into the Mess</td></tr>
        <tr><td class="topics__date">May 19th</td><td>Messy Work</td></tr>
        <tr><td class="topics__date">May 26th</td><td>Messy Church</td></tr>
        <tr><td class="topics__date">June 2nd</td><td>Messy Hospitality</td></tr>
        <tr><td class="topics__date">June 9th</td><td>TBD</td></tr>
        <tr><td class="topics__date">June 16th</td><td>Messy within Boundaries</td></tr>
      </table>
    </div>

    <div class="info info--features">
      <h2 class="info__heading">FEATURES OF<br>THE SERVICE:</h2>
      <ul class="info__list">
        <li>Staffed nursery &amp; children's program every Sunday</li>
        <li>Coffee &amp; snacks</li>
        <li>Everyone welcome</li>
      </ul>
    </div>

    <div class="info info--about">
      <h2 class="info__heading">ABOUT THE<br>CHURCH</h2>
      <p class="info__text">Maple Grove Family Church is a multicultural, multi-generational Christian community, serving Riverton and Lakeview. We are a part of the Northfield Fellowship of Churches.</p>
    </div>

    <footer class="contact-bar">
      <span>Location - 1180 Cedar Line West Riverton, ON&nbsp; L4R 2P8</span>
      <span>Phone-905.555.0142 | Email-info@mgfamilychurch.ca | Website-www.mgfamilychurch.ca</span>
    </footer>
  </section>

</div>
</body>
</html>
```